Gardening and life coaching business card design

I need business cards for a new company in the heart of the Ozarks at the Lake of the Ozarks. Tallow Brook Harvest's mission is to teach the world to fish. We provide fresh local fish and produce using permaculture methods. We work with nature and the flow to create more harmony and less impact. We also coach others who are ready to make this transition. We specialize in microgreens and Aquaculture systems. I would like to make Tallow Brook Harvest come alive with green vines and purple flowers I wold like Tallow Brook Harvest to be in green and the rest of the lettering to be in purple. The feel of the card should be that of the Garden of Eden.

Industry/Entity Type

Life Coaching

Contact Information for Business Card

Tallow Brook Harvest
Owner/Operator Marisol Pettigrew
Contact Info:
(555) 214-9083
tallowbrookharvest.example
tallowbrookharvest is also on FB

```html
<!DOCTYPE html>
<html lang="en">
<head>
<meta charset="utf-8">
<title>Tallow Brook Harvest – Business Card</title>
<link rel="stylesheet" href="https://fonts.googleapis.com/css2?family=Italianno&family=Poiret+One&display=swap">
<style>
  :root {
    --backdrop: #ebebeb;
    --linen: #eeede2;
    --linen-edge: #dddcd0;
    --leaf-green: #8aa66d;
    --slate: #8b8d94;
    --icon-grey: #9a9ca3;
    --emblem-purple: #9a86b4;
    --emblem-green: #a4b87a;
  }
  * { margin: 0; padding: 0; box-sizing: border-box; }
  html, body {
    width: 1200px;
    height: 720px;
    overflow: hidden;
    background: var(--backdrop);
  }
  .canvas {
    position: relative;
    width: 1200px;
    height: 720px;
  }
  .card {
    position: absolute;
    width: 540px;
    height: 309px;
    overflow: hidden;
    background:
      repeating-linear-gradient(0deg, rgba(255,255,255,0.25) 0 1px, transparent 1px 3px),
      repeating-linear-gradient(90deg, rgba(200,198,180,0.18) 0 1px, transparent 1px 3px),
      var(--linen);
    box-shadow: 0 1px 0 var(--linen-edge), 0 6px 18px rgba(0,0,0,0.08);
  }
  /* Contact side */
  .card-contact { left: 40px; top: 70px; }
  .holder-name {
    position: absolute;
    left: 48px;
    top: 36px;
    font-family: "Italianno", cursive;
    font-weight: 400;
    font-size: 70px;
    line-height: 1;
    word-spacing: 8px;
    color: var(--leaf-green);
    white-space: nowrap;
  }
  .holder-role {
    position: absolute;
    left: 236px;
    top: 106px;
    font-family: "Poiret One", sans-serif;
    font-size: 17px;
    color: var(--slate);
  }
  .contact-list {
    position: absolute;
    left: 60px;
    top: 150px;
    list-style: none;
    font-family: "Poiret One", sans-serif;
    font-size: 19px;
    color: var(--slate);
  }
  .contact-list li {
    display: flex;
    align-items: center;
    gap: 10px;
    height: 34px;
    white-space: nowrap;
  }
  .contact-phone { padding-left: 70px; }
  .contact-web { padding-left: 35px; }
  .contact-icon { width: 18px; height: 18px; flex: none; }
  .social-dot {
    width: 26px;
    height: 26px;
    border-radius: 50%;
    background: var(--icon-grey);
    flex: none;
  }
  /* Brand side */
  .card-brand { left: 620px; top: 340px; }
  .brand-emblem {
    position: absolute;
    left: 60px;
    top: 60px;
    width: 220px;
    height: 220px;
    border-radius: 50%;
    background: linear-gradient(160deg, var(--emblem-purple), var(--emblem-green));
  }
  .brand-name {
    position: absolute;
    left: 310px;
    top: 40px;
    font-family: "Italianno", cursive;
    font-weight: 400;
    font-size: 66px;
    line-height: 0.95;
    color: var(--leaf-green);
  }
  .brand-name span { display: block; white-space: nowrap; }
  .brand-name span:nth-child(2) { padding-left: 20px; }
  .brand-name span:nth-child(3) { padding-left: 40px; }
</style>
</head>
<body>
<main class="canvas">
  <section class="card card-contact">
    <h1 class="holder-name">Marisol Pettigrew</h1>
    <p class="holder-role">Owner/Operator</p>
    <ul class="contact-list">
      <li class="contact-phone">
        <svg class="contact-icon" viewBox="0 0 24 24" aria-hidden="true"><path fill="var(--icon-grey)" d="M6.6 10.8a15.1 15.1 0 0 0 6.6 6.6l2.2-2.2c.3-.3.7-.4 1-.2 1.1.4 2.3.6 3.6.6.6 0 1 .4 1 1V20c0 .6-.4 1-1 1A17 17 0 0 1 3 4c0-.6.4-1 1-1h3.5c.6 0 1 .4 1 1 0 1.3.2 2.5.6 3.6.1.3 0 .7-.2 1z"/></svg>
        (555) 214-9083
      </li>
      <li class="contact-web">
        <svg class="contact-icon" viewBox="0 0 24 24" aria-hidden="true"><circle cx="12" cy="12" r="10" fill="var(--icon-grey)"/><path d="M2 12h20M12 2c3 3 3 17 0 20M12 2c-3 3-3 17 0 20" stroke="var(--linen)" stroke-width="1.4" fill="none"/></svg>
        tallowbrookharvest.example
      </li>
      <li class="contact-social">
        <span class="social-dot" aria-hidden="true"></span>
        social.example/tallowbrookharvest
      </li>
    </ul>
  </section>

  <section class="card card-brand">
    <div class="brand-emblem" role="img" aria-label="Brand illustration: bare tree over a watercolour circle in purple and green"></div>
    <h2 class="brand-name"><span>Tallow</span><span>Brook</span><span>Harvest</span></h2>
  </section>
</main>
</body>
</html>
```